New Label Design Project

DetailHi, we are a small Farm growing and selling fresh and dehydrated exotic vegetables to exotic market and ethnic restaurants. We plan to make changes our packaging by using clamshell instead of bags. This is why we send you this project. Our main Target Market are Jamaican, Haitian, Egyptian and Turkish restaurant. Small supermarket Markets like Zentrol, Marquesino, Tollgate Food Market, Kelby food Market.... I sale to reseller in some farmers Market in Florida and Massachusetts. Then we have some direct customers they pick it at the farm stand. We don't have any online presence, my apologies... We are still working on that... We send you different logo. We are still working on the sizes of the clamshell. s for my new Label Design Project will be added soon.

```html
<!DOCTYPE html>
<html lang="en">
<head>
<meta charset="utf-8">
<title>Holloway Farm – Dehydrated Jute Leaves Label</title>
<link href="https://fonts.googleapis.com/css2?family=Lustria&family=Allura&family=Open+Sans:wght@400&family=Roboto+Condensed:wght@500&display=swap" rel="stylesheet">
<style>
  :root {
    --paper: #ffffff;
    --brand-green: #7ea562;
    --ink: #333333;
    --grass-deep: #1db548;
    --grass-mid: #4cbf2c;
    --grass-light: #86d62a;
    --label-white: #ffffff;
  }
  * { margin: 0; padding: 0; box-sizing: border-box; }
  html, body {
    width: 800px;
    height: 1200px;
    overflow: hidden;
    background: var(--paper);
  }
  .label {
    position: relative;
    width: 800px;
    height: 1200px;
    background: var(--paper);
    overflow: hidden;
  }
  .brand-name {
    position: absolute;
    top: 290px;
    width: 100%;
    text-align: center;
    font-family: "Open Sans", sans-serif;
    font-weight: 400;
    font-size: 50px;
    letter-spacing: 1px;
    color: var(--brand-green);
    line-height: 1;
  }
  .product-style {
    position: absolute;
    top: 425px;
    width: 100%;
    text-align: center;
    font-family: "Allura", cursive;
    font-size: 128px;
    color: var(--brand-green);
    line-height: 1;
  }
  .product-name {
    position: absolute;
    top: 568px;
    width: 100%;
    text-align: center;
    font-family: "Lustria", serif;
    font-weight: 400;
    font-size: 100px;
    color: var(--ink);
    line-height: 1;
  }
  .meadow {
    position: absolute;
    left: 0;
    top: 680px;
    width: 800px;
    height: 520px;
  }
  .meadow svg { display: block; }
  .capacity {
    position: absolute;
    left: 40px;
    top: 1066px;
    font-family: "Roboto Condensed", sans-serif;
    font-weight: 500;
    color: var(--label-white);
    text-shadow: 0 1px 3px rgba(0,0,0,0.35);
  }
  .capacity-label {
    display: block;
    font-size: 24px;
    line-height: 1;
    margin-left: 18px;
  }
  .capacity-value {
    display: block;
    font-family: "Open Sans", sans-serif;
    font-size: 46px;
    line-height: 1.05;
  }
  .storage {
    position: absolute;
    left: 252px;
    top: 1073px;
    font-family: "Roboto Condensed", sans-serif;
    font-weight: 500;
    font-size: 31px;
    line-height: 1.15;
    color: var(--label-white);
    text-shadow: 0 1px 3px rgba(0,0,0,0.35);
  }
  .date-box {
    position: absolute;
    left: 603px;
    top: 1020px;
    width: 158px;
    height: 128px;
    background: var(--label-white);
  }
</style>
</head>
<body>
  <main class="label">
    <div class="brand-name">HOLLOWAY FARM</div>

    <div class="product-style">Dehydrated</div>
    <h1 class="product-name">Jute Leaves</h1>

    <div class="meadow" role="img" aria-label="Watercolour illustration of a green grassy meadow">
      <svg width="800" height="520" viewBox="0 0 800 520">
        <defs>
          <linearGradient id="meadowFill" x1="0" y1="0" x2="1" y2="1">
            <stop offset="0" stop-color="#4cbf2c"/>
            <stop offset="0.45" stop-color="#86d62a"/>
            <stop offset="1" stop-color="#1db548"/>
          </linearGradient>
        </defs>
        <path d="M0 90 Q200 60 400 80 T800 70 L800 520 L0 520 Z" fill="url(#meadowFill)"/>
      </svg>
    </div>

    <div class="capacity">
      <span class="capacity-label">HOLDS</span>
      <span class="capacity-value">10oz</span>
    </div>
    <div class="storage">
      KEEP REFRIGERATED<br>
      GARDER RÉFRIGÉRÉ
    </div>
    <div class="date-box" aria-hidden="true"></div>
  </main>
</body>
</html>
```